Foot and ankle surgeon requires a website design

I need a website where prospective and established patients can obtain information and then direct them to making appointments. My practice is a highly professional surgical practice specialising in surgery to the foot and ankle. My title is Mr Colin Dravers, Podiatric Foot & Ankle Surgeon. My qualifications are: BSc MSc FACPS
The practice website will require information on: Locations, phone numbers to make appointments, general background on podiatric surgery,
I would like to include information on: my hospital appointments, surgical fellowships held, training programs undertaken, association memberships, publications written, links to useful websites
A page dedicated to common foot conditions would be useful and also a page with referral information including an online registration section that will be sent direct to the receptionist.
Examples of similar websites include:
http://www.jorbellianfeet.com.au/
http://www.quandrilfootsurgeon.com.au/
I will provide files on logo, self photos and my personal training history etc.
Also if there is going to be a background theme I personally am associated with surfing and beach activities, it would be great if this was able to be reflected in the design.
Thank you.

```html
<!DOCTYPE html>
<html lang="en">
<head>
<meta charset="utf-8">
<title>Mr Colin Dravers – Podiatric Foot &amp; Ankle Surgeon</title>
<link rel="stylesheet" href="https://fonts.googleapis.com/css2?family=Tinos:wght@400;700&family=PT+Sans:wght@400;700&family=Arimo:wght@400;700&family=Questrial&family=Ubuntu:wght@500;700&display=swap">
<style>
  :root {
    --navy: #15457f;
    --blue: #1c5e9f;
    --blue-dark: #0f4682;
    --orange: #ee6a14;
    --orange-dark: #c95410;
    --text: #555b61;
    --ink: #1b1b1b;
    --panel: #c3e4f0;
    --band: #e9f6fb;
    --footer: #3d3d3d;
    --white: #ffffff;
  }
  * { box-sizing: border-box; margin: 0; padding: 0; }
  html, body { width: 927px; height: 1200px; overflow: hidden; background: var(--white); }
  body { position: relative; font-family: "PT Sans", sans-serif; color: var(--text); }
  .abs { position: absolute; }

  /* header */
  .brand-mark { left: 81px; top: 26px; width: 44px; height: 44px; border-radius: 50%; border: 3px solid var(--orange); }
  .brand-name { left: 132px; top: 38px; font-family: "Tinos", serif; font-weight: 700; font-size: 31px; color: var(--navy); line-height: 1; white-space: nowrap; }
  .brand-tag { left: 129px; top: 73px; font-family: "Tinos", serif; font-weight: 700; font-size: 17px; color: var(--orange); white-space: nowrap; }
  .book-link { right: 82px; top: 37px; font-family: "Questrial", sans-serif; font-size: 18px; color: var(--navy); white-space: nowrap; }
  .call-line { right: 79px; top: 68px; display: flex; align-items: center; gap: 7px; font-family: "Questrial", sans-serif; font-size: 17px; color: var(--navy); white-space: nowrap; }
  .call-line .phone-num { font-size: 21px; color: #4a4a4a; font-weight: 700; letter-spacing: 0.5px; }

  /* navigation */
  .main-nav { left: 0; top: 135px; width: 927px; height: 38px; background: linear-gradient(var(--blue), var(--blue-dark)); display: flex; justify-content: center; padding-left: 2px; }
  .main-nav a { font-family: "Arimo", sans-serif; font-size: 11.5px; color: var(--white); text-decoration: none; line-height: 38px; padding: 0 19px; border-right: 1px solid rgba(255,255,255,0.18); }
  .main-nav a:last-child { border-right: none; }

  /* hero */
  .hero-band { left: 0; top: 173px; width: 927px; height: 384px; background: var(--orange); }
  .hero-frame { left: 77px; top: 195px; width: 772px; height: 330px; background: var(--orange-dark); padding: 5px; }
  .hero-photo { width: 100%; height: 100%; background: linear-gradient(120deg, #7a5a4a 0%, #d8a58a 35%, #c98e74 60%, #e3e6ea 100%); }
  .hero-card { left: 95px; top: 278px; width: 343px; height: 164px; background: rgba(245,245,245,0.9); padding: 14px 15px; }
  .hero-card h1 { font-family: "Tinos", serif; font-weight: 400; font-size: 31px; color: var(--navy); line-height: 1.05; }
  .hero-card h2 { font-family: "Tinos", serif; font-weight: 400; font-size: 21px; color: var(--orange); margin-top: 4px; }
  .hero-card p { font-size: 11.5px; color: #3c3c3c; line-height: 15.5px; margin-top: 8px; }

  /* welcome */
  .welcome-title { left: 81px; top: 585px; font-family: "Tinos", serif; font-size: 26px; color: var(--navy); white-space: nowrap; }
  .welcome-copy { left: 81px; top: 628px; width: 473px; font-size: 10.6px; line-height: 18px; }
  .welcome-strong { left: 81px; top: 723px; width: 473px; font-size: 10.6px; line-height: 18px; color: var(--ink); }
  .feature-list { left: 81px; top: 779px; list-style: none; font-family: "Questrial", sans-serif; font-size: 14px; color: var(--navy); }
  .feature-list li { height: 26.5px; }
  .feature-list li::before { content: "»"; margin-right: 6px; }
  .surgery-photo { left: 392px; top: 776px; width: 159px; height: 102px; background: linear-gradient(135deg, #1f6d73, #4ea3a3 50%, #2b5b61); }

  /* appointment form */
  .appt-panel { left: 590px; top: 587px; width: 255px; height: 289px; background: var(--panel); border-radius: 7px; }
  .appt-panel h3 { position: absolute; left: 20px; top: 15px; font-family: "Tinos", serif; font-weight: 700; font-size: 21px; color: var(--navy); white-space: nowrap; }
  .field { position: absolute; left: 22px; width: 200px; height: 27px; background: var(--white); font-family: "Arimo", sans-serif; font-size: 11px; color: #8a8a8a; padding: 8px 9px; }
  .field-label { position: absolute; left: 24px; font-family: "Arimo", sans-serif; font-size: 11px; font-weight: 700; color: #3a3a3a; }
  .select { position: absolute; height: 23px; background: var(--white); border-radius: 4px; font-family: "Arimo", sans-serif; font-size: 11px; color: #8a8a8a; padding: 5px 9px; }
  .select::after { content: "⬍"; position: absolute; right: 6px; top: 4px; font-size: 10px; color: #333; }
  .book-btn { position: absolute; left: 20px; top: 240px; width: 202px; height: 29px; border-radius: 6px; background: linear-gradient(#f47a22, #e05c0d); font-family: "Ubuntu", sans-serif; font-weight: 700; font-size: 17px; letter-spacing: 1px; color: var(--white); text-align: center; line-height: 29px; }

  /* conditions */
  .conditions-band { left: 0; top: 914px; width: 927px; height: 210px; background: var(--band); }
  .conditions-title { left: 91px; top: 926px; font-family: "Tinos", serif; font-size: 23px; color: var(--navy); }
  .condition { position: absolute; top: 977px; width: 150px; text-align: center; }
  .condition-photo { height: 84px; border: 3px solid var(--white); border-radius: 7px; box-shadow: 0 1px 4px rgba(0,0,0,0.25); background: linear-gradient(160deg, #e4e4e4, #c79b86 55%, #b88070); }
  .condition span { display: block; margin-top: 7px; font-family: "Arimo", sans-serif; font-size: 13px; color: var(--navy); }
  .carousel-arrow { top: 1003px; }

  /* footer */
  .site-footer { left: 0; top: 1124px; width: 927px; height: 76px; background: var(--footer); }
  .footer-links { left: 86px; top: 1144px; font-family: "Arimo", sans-serif; font-size: 11px; color: var(--white); white-space: nowrap; word-spacing: 2px; }
  .footer-links i { font-style: normal; margin: 0 12px; }
  .copyright { left: 86px; top: 1166px; font-family: "Arimo", sans-serif; font-size: 11px; color: var(--white); }
  .social { top: 1141px; width: 40px; height: 40px; border-radius: 50%; }
</style>
</head>
<body>

<header>
  <div class="abs brand-mark"></div>
  <div class="abs brand-name">Mr Colin Dravers</div>
  <div class="abs brand-tag">Podiatric Foot &amp; Ankle Surgeon</div>
  <div class="abs book-link">Book An Online Appintment</div>
  <div class="abs call-line">
    <svg width="21" height="21" viewBox="0 0 21 21" aria-hidden="true">
      <circle cx="10.5" cy="10.5" r="10.5" fill="#ee6a14"/>
      <path d="M7 5.5c.6-.4 1.2-.3 1.5.2l1 1.8c.3.5.1 1-.3 1.3l-.6.4c.5 1.2 1.4 2.2 2.6 2.8l.5-.6c.4-.4.9-.5 1.3-.2l1.7 1.1c.5.3.6.9.2 1.4-.9 1.2-2 1.5-3.3.9-2.4-1.1-4.2-3-5.2-5.4-.5-1.3-.2-2.8.6-3.7z" fill="#fff"/>
    </svg>
    <span>Call Now !!</span><span class="phone-num">08 9741 2086</span>
  </div>
</header>

<nav class="abs main-nav">
  <a>HOME</a><a>ABOUT</a><a>PATIENTS</a><a>PODIATRIC SURGERY</a><a>APPOINTMENTS</a><a>BLOG</a><a>FAQ</a><a>CONTACT US</a>
</nav>

<section>
  <div class="abs hero-band"></div>
  <div class="abs hero-frame"><div class="hero-photo" role="img" aria-label="Photo of hands examining a patient's foot"></div></div>
  <div class="abs hero-card">
    <h1>MR.COLIN DRAVERS</h1>
    <h2>Podiatric Foot &amp; Ankle Surgeon</h2>
    <p>Lorem ipsum dolor sit amet, consectetuer adipiscing elit, sed diam nonummy nibh euismod tincidunt ut laoreet dolore magna aliquam erat volutpat.</p>
  </div>
</section>

<section>
  <h2 class="abs welcome-title">Welcome to Mr Colin Dravers</h2>
  <p class="abs welcome-copy">Maecenas tempor, justo id luctus fringilla, nunc ipsum gravida metus, vel tincidunt elit ligula vel dui. Sed eu gravida quam. Aenean tempus, leo at tristique consectetur, elit tortor scelerisque leo, sed sagittis nisl nisl sit amet libero. Curabitur ac libero arcu. Pellentesque adipiscing ultricies consectetur. Donec ullamcorper nunc orci, nec sagittis lectus varius vitae. Sed pharetra enim ac dapibus congue.Etiam egestas imperdiet tellus facilisis luctus. Proin porta justo felis, eget lobortis ligula placerat quis.</p>
  <p class="abs welcome-strong">Sed convallis accumsan nunc, nec tempus sapien venenatis sed. Etiam id scelerisque turpis, et volutpat metus. Praesent semper diam ut magna sollicitudin, at facilisis ante sodales.</p>
  <ul class="abs feature-list">
    <li>Network Design &amp; Installation</li>
    <li>dummy text &amp; printing and typesetting</li>
    <li>been the industry's standard</li>
  </ul>
  <div class="abs surgery-photo" role="img" aria-label="Photo of a surgical team operating"></div>

  <form class="abs appt-panel">
    <h3>Hopital Appointments</h3>
    <div class="field" style="top:55px">Name</div>
    <div class="field" style="top:90px">Contact Number</div>
    <div class="field-label" style="top:126px">Preferred Date?</div>
    <div class="select" style="left:22px;top:146px;width:51px">Day</div>
    <div class="select" style="left:79px;top:146px;width:84px">Month</div>
    <div class="field-label" style="top:181px">Preferred Time?</div>
    <div class="select" style="left:22px;top:197px;width:51px">12</div>
    <div class="select" style="left:83px;top:197px;width:51px">00</div>
    <div class="select" style="left:141px;top:197px;width:51px">am</div>
    <div class="book-btn">Request Booking</div>
  </form>
</section>

<section>
  <div class="abs conditions-band"></div>
  <h2 class="abs conditions-title">Common Foot Conditions</h2>
  <svg class="abs carousel-arrow" style="left:87px" width="14" height="30" viewBox="0 0 14 30" aria-hidden="true"><path d="M12 2 3 15l9 13" fill="none" stroke="#8a9aa6" stroke-width="2"/></svg>
  <div class="condition" style="left:117px"><div class="condition-photo" role="img" aria-label="Photo of a foot in an ankle brace"></div><span>Ankle Replacement</span></div>
  <div class="condition" style="left:295px"><div class="condition-photo" role="img" aria-label="Photo of two bare feet"></div><span>Ankle Trauma</span></div>
  <div class="condition" style="left:473px"><div class="condition-photo" role="img" aria-label="Photo of a foot in an ankle brace"></div><span>Tendom Rupture</span></div>
  <div class="condition" style="left:650px"><div class="condition-photo" role="img" aria-label="Photo of two bare feet"></div><span>Ankle Pain</span></div>
  <svg class="abs carousel-arrow" style="left:816px" width="14" height="30" viewBox="0 0 14 30" aria-hidden="true"><path d="M2 2l9 13-9 13" fill="none" stroke="#8a9aa6" stroke-width="2"/></svg>
</section>

<footer>
  <div class="abs site-footer"></div>
  <div class="abs footer-links">Home<i>|</i>About<i>|</i>Patients<i>|</i>Podiatric Surgery<i>|</i>Appointments<i>|</i>Blog<i>|</i>FAQ</div>
  <div class="abs copyright">Copyright © 2014 Mr Colin Dravers. All rights reserved.</div>
  <div class="abs social" style="left:657px;background:#17406a"></div>
  <div class="abs social" style="left:707px;background:#29a9e1"></div>
  <div class="abs social" style="left:757px;background:#f29111"></div>
  <div class="abs social" style="left:806px;background:#b5b5b5"></div>
</footer>

</body>
</html>
```